Search Fund needs a PowerPoint template design

We need a eye-catching and compelling PowerPoint design for a new company based in Chicago called Tarn Ridge Partners. We are search fund with a primary mission to acquire a founder/family/entrepreneur owned businesses (This is similar to a Private Equity firm). Our goal is to offer investors a unique avenue to invest in an attractive business acquisition while providing business owners with an alternative path to exit. We would like the design to reflect crisp and professional nature that many financial firms present. The template should build on the design of the logo including expanding a logical color palette. The presentation will be used to describe facts regarding the firm, financial data and key messaging that we want our investors and potential partners to takeaway.

Target Market(s)

Financial Investors

Industry/Entity Type

Finance

Font styles to use
Serif
Sans Serif

Colors

Designer to choose colors to be used in the design.

Requirements
Must have
• Should include cover page and slide examples. Attractive data displays (graphs, charts, infographics etc.); Compelling cover; fly pages to put in between sections; table of contents page. Needs to have white space to add text.
Should not have
• Do not redesign the logo or change the logo colors. Additional colors should be added to the PowerPoint template

```html
<!DOCTYPE html>
<html lang="en">
<head>
<meta charset="utf-8">
<title>Tarn Ridge Partners – Presentation Template</title>
<link href="https://fonts.googleapis.com/css2?family=Montserrat:ital,wght@0,400;0,600;0,700;0,800;1,400&family=Open+Sans:wght@400;600&display=swap" rel="stylesheet">
<style>
:root{
  --blue:#1b75c4;
  --blue-dark:#155a9a;
  --navy:#163a63;
  --ink:#2b2b2b;
  --grey:#6d6d6d;
  --grey-light:#b9b9b9;
  --rule:#e2e2e2;
  --yellow:#f6c21c;
  --canvas:#e8e8e8;
  --red:#c0392b;
}
*{box-sizing:border-box;margin:0;padding:0}
html,body{width:1200px;height:1034px;overflow:hidden;background:var(--canvas)}
body{position:relative;font-family:"Open Sans",sans-serif;color:var(--ink)}
.slide{position:absolute;width:290px;height:164px;background:#fff;overflow:hidden;box-shadow:0 1px 3px rgba(0,0,0,.18)}
.c1{left:10px}.c2{left:307px}.c3{left:605px}.c4{left:902px}
.r1{top:5px}.r2{top:176px}.r3{top:347px}.r4{top:518px}.r5{top:689px}.r6{top:859px}
.edge{position:absolute;left:0;top:0;bottom:0;width:5px;background:var(--blue)}
.page{position:absolute;right:7px;top:5px;width:11px;height:13px;background:var(--blue);color:#fff;font:600 3.5px Montserrat,sans-serif;text-align:center;line-height:13px}
.foot{position:absolute;right:8px;bottom:5px;font:700 3.5px Montserrat,sans-serif;color:var(--blue);letter-spacing:.2px}
.title{position:absolute;left:22px;top:9px;font:700 6.8px Montserrat,sans-serif;color:#555;letter-spacing:.2px}
.tx{font-size:3px;line-height:4px;color:var(--grey)}
.abs{position:absolute}
.photo{position:absolute}
.brand{font-family:Montserrat,sans-serif;font-weight:800;color:var(--blue);letter-spacing:.4px}
.brand-sub{font-family:Montserrat,sans-serif;font-weight:400;color:var(--grey);letter-spacing:1.2px}
.h{font-family:Montserrat,sans-serif;font-weight:700}
.ring{position:absolute;border-radius:50%;display:flex;align-items:center;justify-content:center}
.lbl{font:600 3.4px Montserrat,sans-serif;color:#555;text-align:center}
svg{display:block}
</style>
</head>
<body>

<!-- 1 Cover -->
<section class="slide c1 r1">
  <div class="edge"></div>
  <div class="photo" role="img" aria-label="Desk with keyboard, glasses and coffee cup" style="left:120px;top:0;width:170px;height:164px;background:linear-gradient(160deg,#f4f4f4,#dcdcdc 55%,#fafafa)"></div>
  <div class="abs" style="left:38px;top:72px">
    <div class="brand" style="font-size:8px">TARN RIDGE</div>
    <div class="brand-sub" style="font-size:2.6px">PARTNERS</div>
    <div class="h" style="font-size:8.4px;color:#666;margin-top:6px">Presentation Template</div>
    <div style="font-size:5px;color:var(--blue)">Some description of subtitle here</div>
    <div style="margin-top:5px;width:107px;height:7px;border-radius:4px;background:#9a9a9a;color:#fff;font-size:3.5px;text-align:center;line-height:7px">www.tarnridge.example</div>
  </div>
</section>

<!-- 2 Cover blue -->
<section class="slide c2 r1">
  <div class="photo" role="img" aria-label="Grayscale staircase architecture" style="left:0;top:0;width:290px;height:164px;background:linear-gradient(135deg,#cfcfcf,#8b8b8b 60%,#444)"></div>
  <svg class="abs" style="left:0;top:0" width="290" height="164"><polygon points="0,0 150,0 210,130 150,164 0,164" fill="#1b75c4"/><polygon points="150,0 210,130 150,164 0,164 0,150 140,150 190,128 140,0" fill="#155a9a" opacity=".5"/></svg>
  <div class="abs" style="left:18px;top:62px;color:#fff">
    <div class="h" style="font-size:11px;line-height:12px">PRESENTATION<br>TEMPLATE</div>
    <div style="font-size:4.2px;line-height:5px;margin-top:3px;color:#d8e8f8">Place your long style about lorem ipsum<br>dolor sit amet here</div>
    <div style="margin-top:3px;width:96px;height:8px;border-radius:4px;background:var(--yellow);font-size:3.6px;line-height:8px;text-align:center;color:#5a4300">Presented by: Lena Arvik</div>
    <div style="font-size:3.6px;margin-top:4px;color:#d8e8f8">Friday, June 15, 2018</div>
  </div>
  <div class="abs brand" style="right:10px;bottom:10px;font-size:7px;color:#e8f1fb">TARN RIDGE</div>
</section>

<!-- 3 Cover dark -->
<section class="slide c3 r1">
  <div class="photo" role="img" aria-label="Modern glass office building" style="left:0;top:0;width:290px;height:164px;background:linear-gradient(120deg,#5b6a73,#2d3a43 55%,#1b232a)"></div>
  <svg class="abs" style="left:0;top:0" width="290" height="164"><polygon points="110,0 290,0 290,164 150,164" fill="#121a22" opacity=".82"/><polygon points="150,164 170,140 290,140 290,164" fill="#1b75c4"/></svg>
  <div class="abs" style="left:158px;top:54px;color:#fff">
    <div class="h" style="font-size:8.5px">Presentation Template</div>
    <div style="font-size:3.6px;color:#bbb">A Multipurpose Business Pitch Deck</div>
    <div style="font-size:3.6px;color:var(--yellow);margin-top:6px">MAR 2017</div>
    <div style="font-size:3.6px;color:#ddd">PRESENTED BY <span style="color:var(--yellow)">JONAH PELL</span></div>
  </div>
  <div class="abs brand" style="right:10px;bottom:11px;font-size:6.5px;color:#fff">TARN RIDGE</div>
</section>

<!-- 4 Contents -->
<section class="slide c4 r1">
  <div class="photo" role="img" aria-label="Wooden table in a softly lit room" style="left:0;top:0;width:290px;height:164px;background:linear-gradient(180deg,#e9e9e9 0,#cfcfcf 60%,#8c6a4f 75%,#5a3c28)"></div>
  <div class="abs" style="left:130px;top:0;width:160px;height:164px;background:rgba(255,255,255,.82)"></div>
  <div class="h abs" style="left:15px;top:10px;font-size:6.3px;color:#fff">CONTENT AT GLANCE</div>
  <div class="page" style="width:10px">4</div>
  <div class="abs" style="left:122px;top:41px;width:160px;font-size:3.6px;color:#888;line-height:11.8px">
    <div style="display:flex"><span style="width:22px">01</span><span style="flex:1">Self-Awareness</span><span>01</span></div>
    <div style="display:flex"><span style="width:22px">02</span><span style="flex:1">Patience and Integrity</span><span>02</span></div>
    <div style="display:flex"><span style="width:22px">03</span><span style="flex:1">Leadership in The Entry Level</span><span>03</span></div>
    <div style="display:flex"><span style="width:22px">04</span><span style="flex:1">Team Accountability &amp; Reliability</span><span>04</span></div>
    <div style="display:flex"><span style="width:22px">05</span><span style="flex:1">The Value of Questions</span><span>05</span></div>
    <div style="display:flex"><span style="width:22px">06</span><span style="flex:1">Owning Mistakes</span><span>06</span></div>
    <div style="display:flex"><span style="width:22px">07</span><span style="flex:1">Resilience in The Face of Challenges</span><span>07</span></div>
    <div style="display:flex"><span style="width:22px">08</span><span style="flex:1">Utilizing Your Strengths</span><span>08</span></div>
  </div>
  <div class="foot">TARN RIDGE</div>
</section>

<!-- 5 Agenda -->
<section class="slide c1 r2">
  <div class="edge"></div><div class="title">PRESENTATION AGENDA</div><div class="page">5</div>
  <div class="abs" style="left:38px;top:52px;display:grid;grid-template-columns:repeat(3,78px);row-gap:24px">
    <div><svg width="24" height="7"><polygon points="0,0 20,0 24,3.5 20,7 0,7" fill="#2c3e50"/><polygon points="16,0 20,0 24,3.5 20,7 16,7 20,3.5" fill="var(--blue)"/><text x="3" y="5" font-size="4" fill="#fff" font-family="Montserrat">01</text></svg><p class="tx" style="width:55px;margin-top:3px">Contrary to popular belief, this is not simply random text.</p></div>
    <div><svg width="24" height="7"><polygon points="0,0 20,0 24,3.5 20,7 0,7" fill="#2c3e50"/><polygon points="16,0 20,0 24,3.5 20,7 16,7 20,3.5" fill="var(--blue)"/><text x="3" y="5" font-size="4" fill="#fff" font-family="Montserrat">02</text></svg><p class="tx" style="width:55px;margin-top:3px">Contrary to popular belief, this is not simply random text.</p></div>
    <div><svg width="24" height="7"><polygon points="0,0 20,0 24,3.5 20,7 0,7" fill="#2c3e50"/><polygon points="16,0 20,0 24,3.5 20,7 16,7 20,3.5" fill="var(--blue)"/><text x="3" y="5" font-size="4" fill="#fff" font-family="Montserrat">03</text></svg><p class="tx" style="width:55px;margin-top:3px">Contrary to popular belief, this is not simply random text.</p></div>
    <div><svg width="24" height="7"><polygon points="0,0 20,0 24,3.5 20,7 0,7" fill="#2c3e50"/><polygon points="16,0 20,0 24,3.5 20,7 16,7 20,3.5" fill="var(--blue)"/><text x="3" y="5" font-size="4" fill="#fff" font-family="Montserrat">04</text></svg><p class="tx" style="width:55px;margin-top:3px">Contrary to popular belief, this is not simply random text.</p></div>
    <div><svg width="24" height="7"><polygon points="0,0 20,0 24,3.5 20,7 0,7" fill="#2c3e50"/><polygon points="16,0 20,0 24,3.5 20,7 16,7 20,3.5" fill="var(--blue)"/><text x="3" y="5" font-size="4" fill="#fff" font-family="Montserrat">05</text></svg><p class="tx" style="width:55px;margin-top:3px">Contrary to popular belief, this is not simply random text.</p></div>
    <div><svg width="24" height="7"><polygon points="0,0 20,0 24,3.5 20,7 0,7" fill="#2c3e50"/><polygon points="16,0 20,0 24,3.5 20,7 16,7 20,3.5" fill="var(--blue)"/><text x="3" y="5" font-size="4" fill="#fff" font-family="Montserrat">06</text></svg><p class="tx" style="width:55px;margin-top:3px">Contrary to popular belief, this is not simply random text.</p></div>
  </div>
  <div class="foot">TARN RIDGE</div>
</section>

<!-- 6 Short description -->
<section class="slide c2 r2">
  <div class="photo" role="img" aria-label="City skyline seen from an empty road" style="left:0;top:0;width:128px;height:164px;background:linear-gradient(180deg,#eef3f7,#d3dbe1 45%,#8f969b 70%,#5d6165)"></div>
  <div class="h abs" style="left:30px;top:37px;width:95px;text-align:right;font-size:8.8px;line-height:10px;color:#1f1f1f">SHORT DESCRIPTION ABOUT OUR COMPANY</div>
  <div class="page">6</div>
  <div class="abs" style="left:134px;top:36px;width:135px">
    <div class="h" style="font-size:6.6px;font-weight:400;color:#333">Welcome from <b>Our Chief</b></div>
    <div style="font-size:2.8px;color:var(--blue);margin-top:6px;border-bottom:.4px solid var(--blue);width:70px">President and Chief Executive Officer</div>
    <p class="tx" style="margin-top:6px">Vivamus sollicitudin at nisi non malesuada. Aenean cursus vel augue vitae commodo. Integer vulputate nisl a lectus pulvinar, et interdum augue feugiat. Sed eget metus at nunc tincidunt luctus non sed diam.</p>
    <p class="tx" style="margin-top:3px">Proin aliquet accumsan mauris, at ultrices justo lacinia vel. Nullam pretium facilisis dolor, non mattis nulla venenatis a. Donec eget quam ut ante faucibus tempus.</p>
  </div>
  <div class="foot">TARN RIDGE</div>
</section>

<!-- 7 About us -->
<section class="slide c3 r2">
  <div class="edge"></div><div class="title">ABOUT US</div><div class="page">7</div>
  <div class="abs" style="left:54px;top:32px;width:206px">
    <p class="tx">Quisque libero purus, bibendum non quam sit amet, porta interdum est. Aliquam erat volutpat. Morbi sed tellus quis purus placerat facilisis non in enim. Duis et neque nec ligula ultrices.</p>
    <p class="tx" style="margin-top:3px">Through our <span style="color:var(--blue)">operating companies</span>, we deliver lasting value to owners, partners and investors across Chicago and the wider Midwest region.</p>
  </div>
  <div class="abs" style="left:55px;top:80px;width:178px;height:7px;border-radius:4px;background:var(--blue);color:#fff;font-size:3.6px;line-height:7px;text-align:center">VALUE PROPOSITION</div>
  <div class="abs" style="left:58px;top:95px;display:flex;gap:25px">
    <div><div class="ring" style="position:relative;width:17px;height:17px;background:#8a8a8a;margin:0 auto"><svg width="8" height="8" viewBox="0 0 8 8"><circle cx="4" cy="3.2" r="2.5" fill="none" stroke="#fff" stroke-width=".7"/><rect x="3" y="6" width="2" height="1.4" fill="#fff"/></svg></div><div class="lbl" style="margin-top:5px">The Subtitle</div></div>
    <div><div class="ring" style="position:relative;width:17px;height:17px;background:#8a8a8a;margin:0 auto"><svg width="8" height="8" viewBox="0 0 8 8"><rect x="1" y="1" width="6" height="6" fill="none" stroke="#fff" stroke-width=".7"/><path d="M1 4H7M4 1V7" stroke="#fff" stroke-width=".5"/></svg></div><div class="lbl" style="margin-top:5px">The Subtitle</div></div>
    <div><div class="ring" style="position:relative;width:17px;height:17px;background:#8a8a8a;margin:0 auto"><svg width="8" height="8" viewBox="0 0 8 8"><path d="M1.5 6.5L6.5 1.5" stroke="#fff" stroke-width="1"/></svg></div><div class="lbl" style="margin-top:5px">The Subtitle</div></div>
    <div><div class="ring" style="position:relative;width:17px;height:17px;background:#8a8a8a;margin:0 auto"><svg width="8" height="8" viewBox="0 0 8 8"><path d="M1 4L7 1L5 7L4 4.5Z" fill="none" stroke="#fff" stroke-width=".6"/></svg></div><div class="lbl" style="margin-top:5px">The Subtitle</div></div>
  </div>
  <div class="foot">TARN RIDGE</div>
</section>

<!-- 8 Quote -->
<section class="slide c4 r2">
  <svg class="abs" style="left:0;top:0" width="290" height="164" role="img" aria-label="Grayscale upward view of a tall building"><defs><linearGradient id="bldg" x1="0" y1="0" x2="1" y2="1"><stop offset="0" stop-color="#e6e6e6"/><stop offset=".6" stop-color="#9c9c9c"/><stop offset="1" stop-color="#cfcfcf"/></linearGradient></defs><polygon points="0,0 150,0 110,164 0,164" fill="url(#bldg)"/></svg>
  <div class="page">8</div>
  <div class="ring" style="left:206px;top:42px;width:20px;height:20px;background:var(--blue);color:#fff;font:800 9px Montserrat,sans-serif">”</div>
  <div class="abs" style="left:140px;top:69px;width:140px;text-align:center">
    <div style="font:italic 400 7px Montserrat,sans-serif;color:#666">Business that Advances</div>
    <div style="font:italic 400 5px/6px Montserrat,sans-serif;color:var(--blue);margin-top:5px">Sustainable and innovative solutions that help achieve environmental, design, and engineering goals</div>
    <div style="width:26px;height:1px;background:var(--yellow);margin:5px auto 0"></div>
  </div>
  <div class="foot">TARN RIDGE</div>
</section>

<!-- 9 Operation principles -->
<section class="slide c1 r3">
  <div class="edge"></div><div class="title">OPERATION PRINCIPLES</div><div class="page">9</div>
  <div class="ring" style="left:68px;top:48px;width:37px;height:37px;background:#111;border:2px solid #fff;box-shadow:0 0 0 .6px #111"><svg width="14" height="12" viewBox="0 0 14 12"><rect x="1" y="3" width="12" height="8" rx="1" fill="#fff"/><rect x="5" y="1" width="4" height="2" fill="none" stroke="#fff" stroke-width=".8"/></svg></div>
  <div class="ring" style="left:124px;top:42px;width:48px;height:48px;background:var(--blue);border:2px solid #fff;box-shadow:0 0 0 .8px var(--blue)"><svg width="20" height="18" viewBox="0 0 20 18"><polygon points="10,1 19,5 1,5" fill="#fff"/><rect x="3" y="6" width="2" height="8" fill="#fff"/><rect x="9" y="6" width="2" height="8" fill="#fff"/><rect x="15" y="6" width="2" height="8" fill="#fff"/><rect x="1" y="15" width="18" height="2" fill="#fff"/></svg></div>
  <div class="ring" style="left:192px;top:48px;width:37px;height:37px;background:#111;border:2px solid #fff;box-shadow:0 0 0 .6px #111"><svg width="14" height="12" viewBox="0 0 14 12"><polygon points="7,2 13,5 7,8 1,5" fill="#fff"/><path d="M3 6.5V9Q7 11 11 9V6.5" fill="#fff"/></svg></div>
  <div class="abs" style="left:58px;top:96px;width:180px;display:flex;justify-content:space-between;text-align:center">
    <div style="width:55px"><div class="h" style="font-size:5px">Vision</div><p class="tx" style="margin-top:2px">Our vision is to lead with a steady, clear and honest plan.</p></div>
    <div style="width:55px"><div class="h" style="font-size:5px">Core Values</div><p class="tx" style="margin-top:2px">Our values guide how we serve owners and investors daily.</p></div>
    <div style="width:55px"><div class="h" style="font-size:5px">Mission</div><p class="tx" style="margin-top:2px">Our mission is to grow each business we acquire with care.</p></div>
  </div>
  <div class="foot">TARN RIDGE</div>
</section>

<!-- 10 Icon strategy -->
<section class="slide c2 r3">
  <div class="edge"></div><div class="title">ICON STRATEGY LIST</div><div class="page">10</div>
  <p class="tx abs" style="left:22px;top:28px;width:250px">Lorem ipsum dolor sit amet, consectetur adipiscing elit. Through our high performance, low CO<sub>2</sub> concrete mixes and <span style="color:var(--blue)">Certified Sustainability Specialists</span>, we continue to contribute to the building of projects that are environmentally responsible and healthy places to live and work.</p>
  <div class="abs" style="left:22px;top:60px;width:250px;display:flex;justify-content:space-between">
    <div style="width:34px;text-align:center"><div class="ring" style="position:relative;margin:0 auto;width:14px;height:14px;border:.6px solid #999"></div><div style="font-size:3px;color:var(--blue);margin-top:3px">CO2 Emissions</div><p class="tx">Lower impact on every single site.</p></div>
    <div style="width:34px;text-align:center"><div class="ring" style="position:relative;margin:0 auto;width:14px;height:14px;border:.6px solid #999"></div><div style="font-size:3px;color:var(--blue);margin-top:3px">Recyclable</div><p class="tx">Materials reused on every single site.</p></div>
    <div style="width:34px;text-align:center"><div class="ring" style="position:relative;margin:0 auto;width:14px;height:14px;border:.6px solid #999"></div><div style="font-size:3px;color:var(--blue);margin-top:3px">Local Benefits</div><p class="tx">Supply sourced close to each site.</p></div>
    <div style="width:34px;text-align:center"><div class="ring" style="position:relative;margin:0 auto;width:14px;height:14px;border:.6px solid #999"></div><div style="font-size:3px;color:var(--blue);margin-top:3px">Resource Use</div><p class="tx">Less water used on every single site.</p></div>
    <div style="width:34px;text-align:center"><div class="ring" style="position:relative;margin:0 auto;width:14px;height:14px;border:.6px solid #999"></div><div style="font-size:3px;color:var(--blue);margin-top:3px">Energy Efficient</div><p class="tx">Lower energy use on every site.</p></div>
    <div style="width:34px;text-align:center"><div class="ring" style="position:relative;margin:0 auto;width:14px;height:14px;border:.6px solid #999"></div><div style="font-size:3px;color:var(--blue);margin-top:3px">Durability</div><p class="tx">Built to last on every single site.</p></div>
  </div>
  <div class="abs" style="left:22px;top:121px;width:258px;height:7px;background:var(--blue);color:#fff;font:700 3.4px/7px Montserrat,sans-serif;padding-left:2px">CONCRETE IS THE FUTURE OF SUSTAINABLE CONSTRUCTION</div>
  <p class="tx abs" style="left:22px;top:131px;width:255px">Increasingly, concrete is being recognized for its life-cycle environmental and economic benefits, from extraction and production to construction, maintenance and disposal.</p>
  <div class="foot">TARN RIDGE</div>
</section>

<!-- 11 Process -->
<section class="slide c3 r3">
  <div class="edge"></div><div class="title">THE PROCESS</div><div class="page">11</div>
  <div class="abs" style="left:5px;top:28px;width:285px;height:40px;background:#f0f0f0"></div>
  <svg class="abs" style="left:20px;top:34px" width="260" height="20" viewBox="0 0 260 20">
    <path d="M22 12A6 6 0 0 1 34 12" fill="none" stroke="#555" stroke-width="1"/><path d="M28 12L31 7" stroke="#555" stroke-width=".8"/>
    <path d="M50 10H68" stroke="var(--blue)" stroke-width="2"/><polygon points="68,6 74,10 68,14" fill="var(--blue)"/>
    <path d="M95 6L103 14M103 6L95 14" stroke="#555" stroke-width="1"/>
    <path d="M118 10H136" stroke="var(--blue)" stroke-width="2"/><polygon points="136,6 142,10 136,14" fill="var(--blue)"/>
    <circle cx="163" cy="8" r="3" fill="none" stroke="#555" stroke-width=".8"/><circle cx="167" cy="12" r="3" fill="none" stroke="#555" stroke-width=".8"/>
    <path d="M188 10H206" stroke="var(--blue)" stroke-width="2"/><polygon points="206,6 212,10 206,14" fill="var(--blue)"/>
    <rect x="228" y="8" width="10" height="4" fill="none" stroke="#555" stroke-width=".8"/><circle cx="230" cy="13" r="1.5" fill="#555"/><circle cx="237" cy="13" r="1.5" fill="#555"/>
  </svg>
  <div class="abs" style="left:28px;top:57px;width:250px;display:flex;justify-content:space-between">
    <p class="tx" style="width:36px;font-size:2.6px;line-height:3px">Pre-construction review and site planning</p>
    <p class="tx" style="width:36px;font-size:2.6px;line-height:3px">Mix design and material testing stage</p>
    <p class="tx" style="width:36px;font-size:2.6px;line-height:3px">Batching and quality control on site</p>
    <p class="tx" style="width:36px;font-size:2.6px;line-height:3px">Delivery and placement on schedule</p>
  </div>
  <div class="abs" style="left:17px;top:77px;width:122px">
    <div class="h" style="font-size:5.6px;border-bottom:.5px solid #ccc;padding-bottom:2px">Subheading Description</div>
    <p class="tx" style="margin-top:3px;color:#444"><span style="color:var(--blue)">✓</span> Lorem ipsum dolor sit amet, elit consectetur</p>
    <p class="tx" style="color:#444"><span style="color:var(--blue)">✓</span> Nullam pretium facilisis dolor non mattis</p>
    <p class="tx" style="color:#444"><span style="color:var(--blue)">✓</span> Donec eget quam ut ante faucibus tempus</p>
    <p class="tx" style="color:#444"><span style="color:var(--blue)">✓</span> Vivamus sollicitudin at nisi malesuada</p>
    <p class="tx" style="margin-top:3px">Lorem ipsum dolor sit amet, consectetur adipiscing elit. Sed eget metus at nunc tincidunt luctus non sed diam.</p>
  </div>
  <svg class="abs" style="left:145px;top:77px" width="130" height="80" viewBox="0 0 130 80" font-family="Open Sans" font-size="2.6" fill="#777">
    <path d="M8 72H128" stroke="#ccc" stroke-width=".4"/>
    <text x="2" y="4">8</text><text x="2" y="22">6</text><text x="2" y="40">4</text><text x="2" y="58">2</text><text x="2" y="73">0</text>
    <rect x="14" y="36" width="5" height="36" fill="#1f2a3a"/><rect x="20" y="50" width="5" height="22" fill="var(--blue)"/><rect x="26" y="56" width="5" height="16" fill="#aaa"/>
    <rect x="44" y="56" width="5" height="16" fill="#1f2a3a"/><rect x="50" y="30" width="5" height="42" fill="var(--blue)"/><rect x="56" y="48" width="5" height="24" fill="#aaa"/>
    <rect x="74" y="40" width="5" height="32" fill="#1f2a3a"/><rect x="80" y="52" width="5" height="20" fill="var(--blue)"/><rect x="86" y="44" width="5" height="28" fill="#aaa"/>
    <rect x="104" y="24" width="5" height="48" fill="#1f2a3a"/><rect x="110" y="46" width="5" height="26" fill="var(--blue)"/><rect x="116" y="14" width="5" height="58" fill="#aaa"/>
    <text x="18" y="77">2013</text><text x="48" y="77">2014</text><text x="78" y="77">2015</text><text x="108" y="77">2016</text>
  </svg>
  <div class="foot">TARN RIDGE</div>
</section>

<!-- 12 Solutions -->
<section class="slide c4 r3">
  <div class="edge"></div><div class="title">OUR SOLUTIONS</div><div class="page">12</div>
  <div class="abs" style="left:17px;top:29px;width:126px;height:111px;display:grid;grid-template-columns:1fr 1fr;grid-template-rows:1fr 1fr;border-top:.5px solid #ddd;border-bottom:.5px solid #ddd">
    <div style="border-right:.5px solid #ddd;border-bottom:.5px solid #ddd;text-align:center;padding-top:16px"><svg width="12" height="10" style="margin:0 auto" viewBox="0 0 12 10"><path d="M1 2H4L8 8H11M1 8H4L8 2H11" fill="none" stroke="#999" stroke-width=".7"/></svg><div style="font-size:3.8px;color:#888;margin-top:3px">Ready-Mixed<br>Concrete</div></div>
    <div style="border-bottom:.5px solid #ddd;text-align:center;padding-top:16px"><svg width="12" height="10" style="margin:0 auto" viewBox="0 0 12 10"><rect x="3" y="0.5" width="6" height="9" fill="none" stroke="var(--blue-dark)" stroke-width=".7"/><path d="M4.5 3H7.5M4.5 5H7.5M4.5 7H7.5" stroke="var(--blue-dark)" stroke-width=".5"/></svg><div style="font-size:3.8px;color:#888;margin-top:3px">Ready-Mixed<br>Concrete</div></div>
    <div style="border-right:.5px solid #ddd;text-align:center;padding-top:16px"><svg width="12" height="10" style="margin:0 auto" viewBox="0 0 12 10"><circle cx="5" cy="4.5" r="3.5" fill="none" stroke="var(--blue-dark)" stroke-width=".7"/><path d="M7.5 7L10 9.5M3.5 4.5H6.5M5 3V6" stroke="var(--blue-dark)" stroke-width=".7"/></svg><div style="font-size:3.8px;color:#888;margin-top:3px">Value-Added<br>Services</div></div>
    <div style="text-align:center;padding-top:16px"><svg width="12" height="10" style="margin:0 auto" viewBox="0 0 12 10"><polygon points="6,0.5 7.5,3.8 11,4 8.3,6.3 9.2,9.5 6,7.7 2.8,9.5 3.7,6.3 1,4 4.5,3.8" fill="none" stroke="#999" stroke-width=".6"/></svg><div style="font-size:3.8px;color:#888;margin-top:3px">Value-Added<br>Services</div></div>
  </div>
  <div class="abs" style="left:162px;top:31px;width:110px">
    <div class="h" style="font-size:4.2px">Ready-Mixed Concrete</div><p class="tx" style="margin-bottom:8px">We deliver consistent mixes to every job site across the region.</p>
    <div class="h" style="font-size:4.2px">Aggregates</div><p class="tx" style="margin-bottom:8px">Quality sand, gravel and stone supplied from local quarries.</p>
    <div class="h" style="font-size:4.2px">Value-Added Services</div><p class="tx" style="margin-bottom:8px">Testing, planning and on-site support for every project stage.</p>
    <div class="h" style="font-size:4.2px">Specialty Products / Solutions</div><p class="tx">Custom mixes designed for demanding structural requirements.</p>
  </div>
  <div class="foot">TARN RIDGE</div>
</section>

<!-- 13 List point services -->
<section class="slide c1 r4">
  <div class="edge"></div><div class="title">LIST POINT SERVICES</div><div class="page">13</div>
  <div class="abs" style="left:32px;top:42px;width:240px;display:grid;grid-template-columns:repeat(4,60px);row-gap:13px">
    <div style="text-align:center"><div class="ring" style="position:relative;margin:0 auto;width:16px;height:16px;background:var(--navy)"></div><div class="lbl" style="font-size:2.8px;margin-top:3px">Item | Subtitle Here</div><p class="tx" style="font-size:2.6px;line-height:3px">Short note about this service line.</p></div>
    <div style="text-align:center"><div class="ring" style="position:relative;margin:0 auto;width:16px;height:16px;background:#777"></div><div class="lbl" style="font-size:2.8px;margin-top:3px">Item | Subtitle Here</div><p class="tx" style="font-size:2.6px;line-height:3px">Short note about this service line.</p></div>
    <div style="text-align:center"><div class="ring" style="position:relative;margin:0 auto;width:16px;height:16px;background:#aaa"></div><div class="lbl" style="font-size:2.8px;margin-top:3px">Item | Subtitle Here</div><p class="tx" style="font-size:2.6px;line-height:3px">Short note about this service line.</p></div>
    <div style="text-align:center"><div class="ring" style="position:relative;margin:0 auto;width:16px;height:16px;background:var(--blue)"></div><div class="lbl" style="font-size:2.8px;margin-top:3px">Item | Subtitle Here</div><p class="tx" style="font-size:2.6px;line-height:3px">Short note about this service line.</p></div>
    <div style="text-align:center"><div class="ring" style="position:relative;margin:0 auto;width:16px;height:16px;background:var(--blue)"></div><div class="lbl" style="font-size:2.8px;margin-top:3px">Item | Subtitle Here</div><p class="tx" style="font-size:2.6px;line-height:3px">Short note about this service line.</p></div>
    <div style="text-align:center"><div class="ring" style="position:relative;margin:0 auto;width:16px;height:16px;background:var(--navy)"></div><div class="lbl" style="font-size:2.8px;margin-top:3px">Item | Subtitle Here</div><p class="tx" style="font-size:2.6px;line-height:3px">Short note about this service line.</p></div>
    <div style="text-align:center"><div class="ring" style="position:relative;margin:0 auto;width:16px;height:16px;background:#777"></div><div class="lbl" style="font-size:2.8px;margin-top:3px">Item | Subtitle Here</div><p class="tx" style="font-size:2.6px;line-height:3px">Short note about this service line.</p></div>
    <div style="text-align:center"><div class="ring" style="position:relative;margin:0 auto;width:16px;height:16px;background:#aaa"></div><div class="lbl" style="font-size:2.8px;margin-top:3px">Item | Subtitle Here</div><p class="tx" style="font-size:2.6px;line-height:3px">Short note about this service line.</p></div>
  </div>
  <div class="foot">TARN RIDGE</div>
</section>

<!-- 14 US maps -->
<section class="slide c2 r4">
  <div class="edge"></div><div class="title">US MAPS</div><div class="page">14</div>
  <div class="abs" style="left:22px;top:45px;width:82px">
    <div class="h" style="font-size:4.4px;line-height:5px">Ut wisi enim ad minim veniam, quis nostrud exerci</div>
    <p class="tx" style="margin-top:3px">Duis autem vel eum iriure dolor in hendrerit in vulputate velit esse molestie consequat, vel illum dolore eu feugiat nulla facilisis at vero eros.</p>
    <div style="width:22px;height:4px;border-radius:2px;background:var(--blue);margin-top:8px"></div>
  </div>
  <div class="photo" role="img" aria-label="Map of the United States with location pins" style="left:126px;top:48px;width:140px;height:80px;background:radial-gradient(ellipse at 50% 50%,#c4c4c4 55%,#fff 72%)"></div>
  <div class="abs" style="left:181px;top:45px;width:56px;height:9px;background:var(--blue);color:#fff;font-size:2.4px;line-height:3px;padding:1.5px 3px">Chicago office and regional markets</div>
  <div class="foot">TARN RIDGE</div>
</section>

<!-- 15 World maps -->
<section class="slide c3 r4">
  <div class="edge"></div><div class="title">WORLD MAPS</div><div class="page">15</div>
  <div class="photo" role="img" aria-label="World map with North America highlighted" style="left:20px;top:42px;width:148px;height:90px;background:linear-gradient(100deg,#1d2f4a 0,#1d2f4a 32%,#9c9c9c 40%,#8d8d8d 100%);border-radius:40% 30% 35% 40%/30% 40% 45% 35%"></div>
  <div class="abs" style="left:170px;top:40px;height:102px;border-left:.6px dashed var(--red)"></div>
  <div class="abs" style="left:180px;top:50px;width:100px;display:grid;grid-template-columns:1fr 1fr;row-gap:14px;column-gap:6px">
    <div><div style="font:400 10px Montserrat,sans-serif;color:#aaa">15%</div><div class="h" style="font-size:3.8px">Europe</div><p class="tx" style="font-size:2.4px;line-height:3px">Share of total sales in region.</p></div>
    <div><div style="font:400 10px Montserrat,sans-serif;color:#aaa">30%</div><div class="h" style="font-size:3.8px">US</div><p class="tx" style="font-size:2.4px;line-height:3px">Share of total sales in region.</p></div>
    <div><div style="font:400 10px Montserrat,sans-serif;color:#aaa">20%</div><div class="h" style="font-size:3.8px">Africa</div><p class="tx" style="font-size:2.4px;line-height:3px">Share of total sales in region.</p></div>
    <div><div style="font:400 10px Montserrat,sans-serif;color:#aaa">35%</div><div class="h" style="font-size:3.8px">Asia</div><p class="tx" style="font-size:2.4px;line-height:3px">Share of total sales in region.</p></div>
  </div>
  <div class="foot">TARN RIDGE</div>
</section>

<!-- 16 Single list -->
<section class="slide c4 r4">
  <div class="edge"></div><div class="title">TRADITIONAL SINGLE LIST</div><div class="page">16</div>
  <p class="tx abs" style="left:22px;top:26px;width:250px"><b style="color:var(--blue)">Contrary to popular belief,</b> Lorem Ipsum is not simply random text. It has roots in a piece of classical Latin literature from 45 BC.</p>
  <div class="abs" style="left:22px;top:47px;width:250px;border-top:.5px solid #ccc"></div>
  <div class="abs" style="left:36px;top:58px;width:235px">
    <p class="tx" style="margin-bottom:5px"><span style="color:var(--blue);font-size:5px">✓</span> Quisque libero purus, bibendum non quam sit amet, porta interdum est. Aliquam erat volutpat morbi.</p>
    <p class="tx" style="margin-bottom:5px"><span style="color:var(--blue);font-size:5px">✓</span> Praesent a diam neque. Aenean ut arcu cursus, euismod magna at, blandit dui, lobortis quam.</p>
    <p class="tx"><span style="color:var(--blue);font-size:5px">✓</span> Nam auctor leo a volutpat rhoncus, sed porta dignissim velit aliquet lacinia vestibulum.</p>
  </div>
  <p class="tx abs" style="left:25px;top:108px;width:245px">Cras laoreet mauris eget pharetra auctor. Donec lacinia est id euismod eleifend. Quisque condimentum varius ullamcorper nunc quam libero.</p>
  <div class="foot">TARN RIDGE</div>
</section>

<!-- 17 Two column -->
<section class="slide c1 r5">
  <div class="edge"></div><div class="title">TWO COLUMN TEXT</div><div class="page">17</div>
  <p class="tx abs" style="left:22px;top:26px;width:256px;color:#444"><b>Contrary to popular belief,</b> Lorem Ipsum is not simply random text. It has roots in a piece of classical Latin literature from 45 BC. Cras laoreet mauris eget pharetra auctor. Donec lacinia est id euismod eleifend.</p>
  <div class="abs" style="left:22px;top:43px;width:256px;display:grid;grid-template-columns:1fr 1fr;column-gap:8px">
    <p class="tx">Lorem ipsum dolor sit amet, consectetur adipiscing elit. Fusce vitae felis nec enim aliquet tristique. Sed at libero id dui commodo viverra. Mauris euismod risus vel nibh tempus, at pharetra lorem sodales. Curabitur consequat lacus ac quam ultrices, sed euismod tellus rutrum. Donec a orci finibus, bibendum metus et, molestie arcu. Nulla facilisi. Morbi nec sapien vel urna cursus ornare in vitae libero. Integer non nisl ut justo mattis porta.</p>
    <p class="tx">Nulla eget velit sed nisi feugiat molestie. Aenean vitae dui quis risus dictum interdum. Suspendisse potenti. Vestibulum at ante at felis pulvinar convallis. Nam tempus, lacus id lacinia cursus, orci justo gravida mi, a aliquam nisl nisi vel dui. Proin vitae erat eget ipsum dictum placerat at non velit. Etiam tincidunt sem quis sapien mollis, vitae rhoncus risus ultrices.</p>
  </div>
  <div class="foot">TARN RIDGE</div>
</section>

<!-- 18 Three column -->
<section class="slide c2 r5">
  <div class="edge"></div><div class="title">THREE COLUMN TEXT</div><div class="page">18</div>
  <p class="tx abs" style="left:22px;top:26px;width:256px;color:#444"><b>Contrary to popular belief,</b> Lorem Ipsum is not simply random text. It has roots in a piece of classical Latin literature from 45 BC. Cras laoreet mauris eget pharetra auctor.</p>
  <div class="abs" style="left:22px;top:43px;width:256px;display:grid;grid-template-columns:1fr 1fr 1fr;column-gap:7px">
    <p class="tx">Lorem ipsum dolor sit amet, consectetur adipiscing elit. Fusce vitae felis nec enim aliquet tristique. Sed at libero id dui commodo viverra. Mauris euismod risus vel nibh tempus, at pharetra lorem sodales quam.</p>
    <p class="tx">Curabitur consequat lacus ac quam ultrices, sed euismod tellus rutrum. Donec a orci finibus, bibendum metus et, molestie arcu. Nulla facilisi. Morbi nec sapien vel urna cursus ornare in vitae libero.</p>
    <p class="tx">Nulla eget velit sed nisi feugiat molestie. Aenean vitae dui quis risus dictum interdum. Suspendisse potenti. Vestibulum at ante at felis pulvinar convallis. Nam tempus lacus id lacinia cursus.</p>
  </div>
  <div class="foot">TARN RIDGE</div>
</section>

<!-- 19 Section break navy -->
<section class="slide c3 r5">
  <div class="photo" role="img" aria-label="Hand holding a cup of coffee" style="left:0;top:0;width:150px;height:164px;background:radial-gradient(circle at 40% 40%,#c9a58b,#7a5a48 45%,#2a2420 85%)"></div>
  <div class="abs" style="left:150px;top:0;width:140px;height:164px;background:var(--navy)"></div>
  <div class="abs" style="left:132px;top:0;width:18px;height:164px;background:rgba(27,117,196,.55)"></div>
  <div class="ring" style="left:206px;top:48px;width:28px;height:28px;border:1.3px solid #fff;color:#fff;font:700 12px Georgia,serif">i</div>
  <div class="abs" style="left:160px;top:82px;width:120px;text-align:center;color:#fff">
    <div class="h" style="font-size:8.4px">Section Break</div>
    <p style="font-size:3px;line-height:3.8px;color:#c8d5e4;margin-top:3px">The quick brown fox jumps over a lazy dog. Our fund invests in durable owner-led firms.</p>
  </div>
  <div class="abs brand" style="left:6px;bottom:8px;font-size:5px;color:#fff">TARN RIDGE</div>
</section>

<!-- 20 Section break photo -->
<section class="slide c4 r5">
  <div class="photo" role="img" aria-label="Blurred café interior with wooden table" style="left:0;top:0;width:290px;height:164px;background:linear-gradient(180deg,#3b3a38 0,#5a5048 50%,#8a6a4a 75%,#4a3828)"></div>
  <svg class="abs" style="left:0;top:0" width="290" height="164"><polygon points="160,0 290,0 290,164 110,164" fill="#1a1e24" opacity=".85"/><polygon points="148,72 290,72 290,88 136,88" fill="var(--blue-dark)"/></svg>
  <div class="h abs" style="left:180px;top:75px;width:100px;text-align:center;font-size:8.4px;color:#fff">Section Break</div>
  <div class="abs" style="left:180px;top:97px;width:100px;text-align:center">
    <div style="font:400 5.2px Montserrat,sans-serif;color:var(--yellow)">10.45 – 11.00</div>
    <div class="brand" style="font-size:4px;color:#fff;margin-top:3px">TARN RIDGE</div>
    <p style="font-size:2.8px;line-height:3.4px;color:#bbb;margin-top:4px">The quick brown fox jumps over a lazy dog. Our fund invests in owner-led firms.</p>
  </div>
</section>

<!-- 21 Section break light -->
<section class="slide c1 r6">
  <div class="abs" style="left:125px;top:0;width:8px;height:80px;background:#9a9a9a"></div>
  <div class="abs" style="left:133px;top:0;width:8px;height:80px;background:var(--blue)"></div>
  <div class="abs" style="left:122px;top:84px">
    <div class="brand" style="font-size:7.4px">TARN RIDGE</div>
    <div class="brand-sub" style="font-size:2.4px">PARTNERS</div>
    <div style="font:400 7.6px Montserrat,sans-serif;color:#e0a800;margin-top:2px">Section Break</div>
    <div style="font:400 5.6px Montserrat,sans-serif;color:#999;border-top:.5px solid #ddd;margin-top:3px;padding-top:2px">10.45 – 11.00</div>
    <p class="tx" style="width:80px;margin-top:5px;color:#333">The quick brown fox jumps over a lazy dog. Our fund invests in owner-led firms.</p>
  </div>
</section>

<!-- 22 Annual report table -->
<section class="slide c2 r6">
  <div class="edge"></div><div class="title">ANNUAL REPORT TABLE</div><div class="page">21</div>
  <div class="ring" style="left:14px;top:42px;width:22px;height:22px;border:.8px solid #222"><svg width="10" height="10" viewBox="0 0 10 10"><path d="M1 1L9 9M9 1L1 9" stroke="#222" stroke-width="1"/></svg></div>
  <div class="ring" style="left:44px;top:42px;width:22px;height:22px;border:.8px solid #222"><svg width="10" height="10" viewBox="0 0 10 10"><path d="M5 4V10" stroke="#222" stroke-width="1"/><path d="M3 0V3Q5 5 7 3V0" fill="none" stroke="#222" stroke-width=".8"/></svg></div>
  <div class="abs" style="left:82px;top:45px;width:140px">
    <div class="h" style="font-size:4.6px;color:var(--blue)">Company budget files 2019</div>
    <p class="tx" style="font-size:2.6px;line-height:3.2px">Lorem ipsum dolor sit amet, consectetur adipiscing elit. Sed eget metus at nunc tincidunt luctus non sed diam donec.</p>
  </div>
  <table class="abs" style="left:14px;top:69px;width:212px;border-collapse:collapse;font-size:2.8px;color:#555">
    <tr style="color:#e0a800;border-bottom:.5px solid #ccc"><td style="height:6px">Miscellaneous budget</td><td>2014</td><td>2015</td><td>2016</td><td>2017</td></tr>
    <tr style="border-bottom:.4px solid #eee"><td style="height:9px">Project cost / estimate</td><td>4,367</td><td>4,435</td><td>4,567</td><td>4,564</td></tr>
    <tr style="border-bottom:.4px solid #eee"><td style="height:9px">Project cost / estimate</td><td>5,345</td><td>5,341</td><td>5,542</td><td>5,343</td></tr>
    <tr style="border-bottom:.4px solid #eee"><td style="height:9px">Project cost / estimate</td><td>6,787</td><td>6,765</td><td>6,090</td><td>6,327</td></tr>
    <tr style="border-bottom:.4px solid #eee"><td style="height:9px">Project cost / estimate</td><td>7,876</td><td>7,678</td><td>7,678</td><td>7,870</td></tr>
    <tr style="border-bottom:.4px solid #eee"><td style="height:9px">Project cost / estimate</td><td>5,789</td><td>5,789</td><td>5,789</td><td>5,783</td></tr>
    <tr><td style="height:7px;color:var(--blue)">CHANGE 45%</td><td></td><td></td><td></td><td></td></tr>
  </table>
  <div class="abs" style="left:230px;top:45px;width:60px;height:100px;background:#3f7fb8;color:#dbe8f5;font-size:3.2px;line-height:4px">
    <div style="background:#1d2533;color:#fff;padding:2px 4px;font-size:3px">STATS MANAGER</div>
    <div style="padding:3px 4px;border-bottom:.5px solid #9cc0e2">THIS YEAR<br>17,759</div>
    <div style="padding:3px 4px;border-bottom:.5px solid #9cc0e2">THIS MONTH<br>3,000</div>
    <div style="padding:3px 4px;border-bottom:.5px solid #9cc0e2">THIS WEEK<br>450</div>
    <div style="padding:3px 4px">TODAY<br>225</div>
  </div>
  <div class="foot">TARN RIDGE</div>
</section>

<!-- 23 Contact -->
<section class="slide c3 r6">
  <div class="edge"></div><div class="title">CONTACT US</div><div class="page">22</div>
  <p class="abs" style="left:22px;top:27px;font-size:3.8px;color:#666">Need assistance or have a question? Let us help. Contact our office today.</p>
  <div class="abs" style="left:22px;top:46px;width:230px;border-top:.5px solid #ccc"></div>
  <div class="abs" style="left:24px;top:54px;display:flex;gap:4px">
    <svg width="8" height="8" viewBox="0 0 8 8"><rect width="8" height="8" fill="#222"/><path d="M4 1.5A1.8 1.8 0 0 1 5.8 3.3C5.8 4.8 4 6.5 4 6.5S2.2 4.8 2.2 3.3A1.8 1.8 0 0 1 4 1.5Z" fill="#fff"/></svg>
    <div><div style="font-size:2.6px;color:#999">Contact office</div><div class="h" style="font-size:3.8px">Head Office</div><p class="tx" style="font-size:2.6px;line-height:3.2px">400 West Lake Street, Suite 12<br>Chicago, IL 60606<br>Tel: 312-555-0148</p></div>
  </div>
  <div class="abs" style="left:152px;top:54px;display:flex;gap:4px">
    <svg width="8" height="8" viewBox="0 0 8 8"><circle cx="2" cy="4" r="1.2" fill="var(--blue)"/><circle cx="6" cy="1.8" r="1.2" fill="var(--blue)"/><circle cx="6" cy="6.2" r="1.2" fill="var(--blue)"/><path d="M2 4L6 1.8M2 4L6 6.2" stroke="var(--blue)" stroke-width=".6"/></svg>
    <div><div style="font-size:2.6px;color:#999">Follow us on</div><div class="h" style="font-size:3.8px">Social Share</div>
      <p class="tx" style="font-size:2.6px;line-height:3.6px"><span style="display:inline-block;width:2.4px;height:2.4px;border-radius:50%;background:#555"></span> tarnridge<br><span style="display:inline-block;width:2.4px;height:2.4px;border-radius:50%;background:#555"></span> @tarnridge<br><span style="display:inline-block;width:2.4px;height:2.4px;border-radius:50%;background:#555"></span> tarn-ridge</p></div>
  </div>
  <div class="photo" role="img" aria-label="Glass building facade with sunlight" style="left:8px;top:116px;width:282px;height:48px;background:linear-gradient(100deg,#173a6a,#2f6fb0 40%,#9db8d2 65%,#f1c76a 80%,#234a7a)"></div>
</section>

<!-- 24 Thank you -->
<section class="slide c4 r6">
  <div class="abs" style="left:0;top:46px;width:290px;text-align:center">
    <div class="brand" style="font-size:12px">TARN RIDGE</div>
    <div class="brand-sub" style="font-size:3px">PARTNERS</div>
    <div class="h" style="font-size:9.4px;color:#666;margin-top:5px;font-weight:600">Thank You</div>
    <div style="width:190px;margin:3px auto 0;border-top:.6px solid #333"></div>
    <p class="tx" style="width:165px;margin:4px auto 0">Contrary to popular belief, Lorem Ipsum is not simply random text. It has roots in classical Latin literature from 45 BC, making it over two thousand years old.</p>
  </div>
  <div class="foot">TARN RIDGE</div>
</section>

</body>
</html>
```